Business Card Design Project

New business card design front and back for IT company that does network support and web design.
Calloway IT
Derek Calloway
Managing Director
PO Box 582 Tarrowby VIC 3267
derek@callowayit.example
www.callowayit.example

Industry/Entity Type

Business

```html
<!DOCTYPE html>
<html lang="en">
<head>
<meta charset="utf-8">
<title>Calloway IT — Business Cards</title>
<link rel="stylesheet" href="https://fonts.googleapis.com/css2?family=Open+Sans:wght@400;600;700&display=swap">
<style>
  :root {
    --brand-blue: #2aa3d4;
    --brand-blue-deep: #1b8cc0;
    --ink: #1d1e21;
    --paper: #eef0f1;
    --rule: #b9bfc3;
    --backdrop: #e4e2df;
    --white: #ffffff;
  }
  * { box-sizing: border-box; margin: 0; padding: 0; }
  html, body {
    width: 1200px; height: 880px; overflow: hidden;
    background: var(--backdrop);
    font-family: "Open Sans", Arial, sans-serif;
  }
  .canvas {
    width: 1200px; height: 880px;
    display: flex; flex-direction: column; align-items: center; justify-content: center;
    gap: 44px;
  }
  .card {
    width: 640px; height: 388px; position: relative; overflow: hidden;
    box-shadow: 0 6px 18px rgba(0,0,0,.18);
  }

  /* Front */
  .card-front {
    background: linear-gradient(180deg, var(--brand-blue) 0%, var(--brand-blue-deep) 100%);
    display: flex; align-items: center; justify-content: space-between;
    padding: 0 46px 0 54px;
  }
  .brand { display: flex; align-items: center; gap: 14px; }
  .brand-mark { width: 22px; height: 22px; background: var(--ink); }
  .brand-name {
    color: var(--paper); font-weight: 600; font-size: 34px; letter-spacing: .5px;
    text-transform: uppercase; white-space: nowrap;
  }
  .tagline { color: var(--white); }
  .tagline-main { font-weight: 700; font-size: 42px; line-height: 1; }
  .tagline-sub {
    color: var(--ink); font-weight: 700; font-size: 18px; margin-top: 8px; letter-spacing: .2px;
  }

  /* Back */
  .card-back { background: var(--paper); }
  .back-band {
    position: absolute; left: 0; top: 0; width: 100%; height: 176px;
    background: linear-gradient(180deg, var(--brand-blue) 0%, var(--brand-blue-deep) 100%);
    display: flex; align-items: flex-end; justify-content: flex-end;
    padding: 0 36px 34px 0;
  }
  .back-band .brand-name { font-size: 30px; }
  .back-stripe {
    position: absolute; left: 0; top: 176px; width: 100%; height: 14px; background: var(--ink);
  }
  .identity { position: absolute; left: 34px; top: 212px; width: 572px; }
  .person-name { color: var(--brand-blue-deep); font-weight: 700; font-size: 22px; }
  .name-rule { height: 1px; background: var(--rule); margin: 6px 0 6px; }
  .person-role { color: var(--ink); font-size: 15px; }
  .contact-list {
    position: absolute; left: 270px; top: 272px; list-style: none;
    color: var(--ink); font-size: 17px; line-height: 1.55;
  }
  .contact-list li { display: flex; align-items: center; gap: 10px; }
  .contact-icon { width: 16px; height: 16px; flex: none; fill: var(--brand-blue-deep); }
  .contact-rule {
    position: absolute; left: 34px; right: 34px; top: 350px; height: 1px; background: var(--rule);
  }
</style>
</head>
<body>
<main class="canvas">

  <section class="card card-front" aria-label="Card front">
    <div class="brand">
      <span class="brand-mark"></span>
      <span class="brand-name">Calloway IT</span>
    </div>
    <div class="tagline">
      <p class="tagline-main">IT Solutions</p>
      <p class="tagline-sub">FOR YOUR BUSINESS</p>
    </div>
  </section>

  <section class="card card-back" aria-label="Card back">
    <div class="back-band">
      <div class="brand">
        <span class="brand-mark"></span>
        <span class="brand-name">Calloway IT</span>
      </div>
    </div>
    <div class="back-stripe"></div>

    <div class="identity">
      <p class="person-name">Derek Calloway</p>
      <div class="name-rule"></div>
      <p class="person-role">Managing Director</p>
    </div>

    <ul class="contact-list">
      <li>
        <svg class="contact-icon" viewBox="0 0 16 16" aria-hidden="true"><path d="M8 1 1 7.5h2V15h4v-4h2v4h4V7.5h2z"/></svg>
        PO Box 582 Tarrowby VIC 3267
      </li>
      <li>
        <svg class="contact-icon" viewBox="0 0 16 16" aria-hidden="true"><path d="M1 3h14v10H1z M2 4l6 5 6-5" fill="none" stroke="#1b8cc0" stroke-width="1.6"/></svg>
        derek@callowayit.example
      </li>
      <li>
        <svg class="contact-icon" viewBox="0 0 16 16" aria-hidden="true"><circle cx="8" cy="8" r="6.5" fill="none" stroke="#1b8cc0" stroke-width="1.5"/><path d="M1.5 8h13M8 1.5c-3 3.5-3 9.5 0 13M8 1.5c3 3.5 3 9.5 0 13" fill="none" stroke="#1b8cc0" stroke-width="1.2"/></svg>
        www.callowayit.example
      </li>
    </ul>
    <div class="contact-rule"></div>
  </section>

</main>
</body>
</html>
```